Flyer Frost Glow Cycle Tour
Zielgruppe
Wir sind DER Bikeshop in St. Moritz, welches auf 1800 m.ü.m. liegt. Wir verkaufen, vermieten uns servicen Bikes das ganze Jahr hindurch und haben auch 365 Tage im Jahr geöffnet. Wir sind die ersten, welche das Winterbiken für alle zugänglich gemacht haben und mit unseren Durafelt E-MTB ist das Fahren auf dem Schnee erstens sehr einfach und zweitens absolut sicher.
Aufgabenstellung
Flyerformat ist egal. Unsere Geschäftsfarben sind schwarz und gelb, der Hauptfont unseres Namens ist Marvelouz und wir arbeiten im High End Bereich. Gerne zwei Sprachen verwenden, evtl. Rückseite und Vorderseite gleich, nur die Sprachen ändern.
TEXT:
St. Moritz
Frost Glow Cycle Tour
Im Winter zu Biken ist ja schon verrückt, aber das ganze in der Nacht zu machen scheint ein Ding der Unmöglichkeit. Es ist das wahrscheinlich eines der coolsten Erlebnisse, welches es in St. Moritz im Winter gibt. Dank den Durafelt E-Bikes mit Spikes und unseren tollen Guides können Sie diese Ausfahrt auch sehr sicher erleben und sie ist für alle Personen, egal welchen Alters geeignet.
Auf speziellen Wunsch organisieren wir auch ein Outdoor-Abendessen, eine versteckte Alphütte zum Essen und Partymachen oder ganz einfach eine Champagnerpause im Pulverschnee dazu.
Dauer
1.5 – 2 Stunden
Inbegriffen
High End E-Bikes von Durafelt, Helm, Stirnlampe, heisses Getränk, Guide
Preis
ab Fr. 95.- pro Person (bei 8 Teilnehmern), Fr. 97.- bei 7 T., Fr. 100.- bei 6 T., Fr. 104.- bei 5 T., Fr. 110.- bei 4 T., Fr. 120.- bei 3 T., Fr. 140.- bei 2 T., Fr. 200.- bei einem Teilnemer.
Biking in winter is already crazy, but doing it at night seems impossible. It’s probably one of the coolest experiences you can have in St. Moritz in winter. Thanks to the Durafelt e-bikes with spikes and our great guides, you can also experience this ride very safely and it is suitable for all people, no matter what age.
On special request, we can also organise an outdoor dinner, a hidden alpine hut for eating and partying or simply a champagne break in the powder snow.
Duration
Included
High End E-Bikes von Durafelt, Helm, Stirnlampe, heisses Getränk, ..

```html
<!DOCTYPE html>
<html lang="de">
<head>
<meta charset="utf-8">
<title>Frost Glow Cycle Tour – Flyer</title>
<link rel="stylesheet" href="https://fonts.googleapis.com/css2?family=Alfa+Slab+One&family=Montserrat:wght@400;500;600;700&display=swap">
<style>
  :root {
    --canvas: #eeeeee;
    --night: #1f1f23;
    --yellow: #edc21f;
    --navy: #1f3f78;
    --white: #ffffff;
    --paper: #f2f2f2;
    --ink: #2a2a2a;
  }
  * { box-sizing: border-box; margin: 0; padding: 0; }
  html, body { width: 1200px; height: 1200px; overflow: hidden; background: var(--canvas); }
  body { font-family: "Montserrat", sans-serif; position: relative; }

  .flyer {
    position: absolute; left: 200px; top: 35px;
    width: 800px; height: 1130px;
    background: var(--night); overflow: hidden;
    box-shadow: 0 10px 30px rgba(0,0,0,.25);
  }
  .hero-photo {
    position: absolute; left: 0; top: 0; width: 800px; height: 600px;
    background:
      radial-gradient(ellipse at 45% 28%, rgba(214,150,70,.55), transparent 45%),
      radial-gradient(ellipse at 60% 62%, rgba(225,225,240,.45), transparent 55%),
      linear-gradient(180deg, #3a2e2a 0%, #2c2a30 45%, #4a3c48 70%, var(--night) 100%);
  }
  .brand {
    position: absolute; top: 48px; left: 0; width: 100%;
    display: flex; justify-content: center; align-items: center; gap: 12px;
  }
  .brand-dot { width: 18px; height: 18px; border-radius: 50%; background: var(--white); }
  .brand-name {
    font-family: "Montserrat", sans-serif; font-weight: 700;
    font-size: 30px; letter-spacing: 10px; color: var(--white);
  }
  .title-place {
    position: absolute; top: 300px; left: 0; width: 100%; text-align: center;
    font-family: "Alfa Slab One", serif; font-size: 60px; color: var(--navy);
    -webkit-text-stroke: 2px var(--white); paint-order: stroke fill;
    text-shadow: 0 3px 0 var(--white);
  }
  .ribbon { position: absolute; top: 385px; left: 115px; width: 570px; height: 78px; }
  .ribbon-text {
    position: absolute; top: 402px; left: 0; width: 100%; text-align: center;
    font-family: "Alfa Slab One", serif; font-size: 27px; letter-spacing: 2px; color: var(--night);
  }
  .intro {
    position: absolute; top: 490px; left: 110px; width: 580px;
    color: var(--white); font-size: 12.5px; line-height: 1.75; text-align: center;
  }
  .intro p + p { margin-top: 12px; }
  .intro .accent { color: var(--yellow); }

  .offer { position: absolute; left: 0; top: 680px; width: 800px; height: 450px; background: var(--yellow); }
  .included {
    position: absolute; left: 0; top: 0; width: 800px; height: 40px; background: var(--navy);
    color: var(--white); font-weight: 700; font-size: 13px; letter-spacing: .3px;
    display: flex; align-items: center; justify-content: center; text-transform: uppercase;
  }
  .best-deal {
    position: absolute; left: 70px; top: 75px; width: 180px; height: 150px;
    border: 2px solid var(--navy); border-radius: 10px; text-align: center; color: var(--navy);
  }
  .best-deal-head {
    background: var(--navy); color: var(--white); border-radius: 7px 7px 0 0;
    font-family: "Alfa Slab One", serif; font-size: 18px; padding: 6px 0; letter-spacing: 1px;
  }
  .best-deal-price { font-family: "Alfa Slab One", serif; font-size: 38px; margin-top: 8px; }
  .best-deal-price small, .tier-price small { font-size: .45em; margin-right: 3px; }
  .best-deal-note { font-size: 16px; line-height: 1.3; }

  .tier { position: absolute; width: 100px; text-align: center; color: var(--navy); }
  .tier-price { font-family: "Alfa Slab One", serif; font-size: 20px; }
  .tier-note { font-size: 9px; line-height: 1.35; color: var(--ink); }
  .duration {
    position: absolute; left: 610px; top: 70px; width: 125px; height: 60px;
    background: var(--navy); border-radius: 10px; color: var(--white);
    font-weight: 600; font-size: 16px; line-height: 1.25; text-align: center;
    display: flex; align-items: center; justify-content: center;
  }

  .footer-wave { position: absolute; left: 0; top: 245px; width: 800px; height: 205px; }
  .photos { position: absolute; left: 55px; top: 262px; width: 690px; display: flex; justify-content: space-between; }
  .photo {
    width: 210px; height: 140px; border-radius: 14px; border: 5px solid var(--white);
    box-shadow: 0 4px 10px rgba(0,0,0,.25);
  }
  .photo-town { background: linear-gradient(180deg, #2c3d66 0%, #6c7aa0 45%, #c99a4a 80%, #3a3550 100%); }
  .photo-fire { background: linear-gradient(180deg, #233a6a 0%, #3c4c7a 40%, #e0a040 75%, #f0d8b8 100%); }
  .photo-riders { background: linear-gradient(180deg, #1c2438 0%, #4c5a70 45%, #c8ccd8 80%, #eaeaf0 100%); }

  .contacts {
    position: absolute; left: 50px; top: 400px; width: 700px;
    display: flex; justify-content: space-between; align-items: center;
    font-size: 13px; font-weight: 600; color: var(--ink);
  }
  .contact { display: flex; align-items: center; gap: 7px; }
  .contact svg { width: 16px; height: 16px; }
</style>
</head>
<body>
  <main class="flyer">
    <div class="hero-photo" role="img" aria-label="Group of riders with headlamps on e-bikes in the snow at night above the lit town of St. Moritz"></div>

    <div class="brand">
      <span class="brand-dot"></span>
      <span class="brand-name">TRAILHAUS</span>
    </div>

    <h1 class="title-place">ST. MORITZ</h1>

    <svg class="ribbon" viewBox="0 0 570 78" aria-hidden="true">
      <polygon points="0,8 570,8 548,39 570,70 0,70 22,39" fill="#edc21f"/>
    </svg>
    <h2 class="ribbon-text">FROST GLOW CYCLE TOUR</h2>

    <section class="intro">
      <p>Im Winter zu Biken ist ja schon verrückt, aber das ganze in der Nacht zu machen scheint ein Ding der Unmöglichkeit. Es ist das wahrscheinlich eines der coolsten Erlebnisse, welches es in <span class="accent">St. Moritz</span> im Winter gibt. Dank den Durafelt E-Bikes mit Spikes und unseren tollen Guides können Sie diese Ausfahrt auch sehr sicher erleben und sie ist für alle Personen, egal welchen Alters geeignet.</p>
      <p>Auf speziellen Wunsch organisieren wir auch ein Outdoor-Abendessen, eine versteckte Alphütte zum Essen und Partymachen oder ganz einfach eine Champagnerpause im Pulverschnee dazu.</p>
    </section>

    <section class="offer">
      <div class="included">Inbegriffen: High End E-Bikes von Durafelt, Helm, Stirnlampe, heisses Getränk, Guide</div>

      <div class="best-deal">
        <div class="best-deal-head">BEST DEAL!</div>
        <div class="best-deal-price"><small>FR.</small>95.-</div>
        <div class="best-deal-note">pro Person<br>(bei 8 Teilnehmern)</div>
      </div>

      <div class="tier" style="left:290px;top:85px"><div class="tier-price"><small>FR.</small>97.-</div><div class="tier-note">pro Person<br>(bei 7 Teilnehmern)</div></div>
      <div class="tier" style="left:395px;top:85px"><div class="tier-price"><small>FR.</small>100.-</div><div class="tier-note">pro Person<br>(bei 6 Teilnehmern)</div></div>
      <div class="tier" style="left:500px;top:85px"><div class="tier-price"><small>FR.</small>104.-</div><div class="tier-note">pro Person<br>(bei 5 Teilnehmern)</div></div>
      <div class="duration">Dauer:<br>2 Stunden</div>

      <div class="tier" style="left:290px;top:160px"><div class="tier-price"><small>FR.</small>110.-</div><div class="tier-note">pro Person<br>(bei 4 Teilnehmern)</div></div>
      <div class="tier" style="left:395px;top:160px"><div class="tier-price"><small>FR.</small>120.-</div><div class="tier-note">pro Person<br>(bei 3 Teilnehmern)</div></div>
      <div class="tier" style="left:500px;top:160px"><div class="tier-price"><small>FR.</small>140.-</div><div class="tier-note">pro Person<br>(bei 2 Teilnehmern)</div></div>
      <div class="tier" style="left:622px;top:160px"><div class="tier-price"><small>FR.</small>200.-</div><div class="tier-note">(bei 1 Teilnehmer)</div></div>

      <svg class="footer-wave" viewBox="0 0 800 205" preserveAspectRatio="none" aria-hidden="true">
        <path d="M0,110 Q400,0 800,110 L800,205 L0,205 Z" fill="#f2f2f2"/>
      </svg>

      <div class="photos">
        <div class="photo photo-town" role="img" aria-label="Evening view of the snowy town of St. Moritz below the mountains"></div>
        <div class="photo photo-fire" role="img" aria-label="Campfire with a hanging grill in the snow at dusk"></div>
        <div class="photo photo-riders" role="img" aria-label="Riders with e-bikes among lit trees at night"></div>
      </div>

      <div class="contacts">
        <span class="contact">
          <svg viewBox="0 0 16 16"><path d="M8 1a5 5 0 0 0-5 5c0 4 5 9 5 9s5-5 5-9a5 5 0 0 0-5-5zm0 7a2 2 0 1 1 0-4 2 2 0 0 1 0 4z" fill="#1f3f78"/></svg>
          Via Sulai 14 7500 St. Moritz
        </span>
        <span class="contact">
          <svg viewBox="0 0 16 16"><path d="M4 1l3 3-2 2c1 2 3 4 5 5l2-2 3 3-2 3C7 15 1 9 1 3z" fill="#1f3f78"/></svg>
          +41 81 555 01 20
        </span>
        <span class="contact">
          <svg viewBox="0 0 16 16"><rect x="1" y="3" width="14" height="10" fill="#1f3f78"/><path d="M1 3l7 6 7-6" fill="none" stroke="#fff" stroke-width="1.3"/></svg>
          tour@trailhaus.ch
        </span>
        <span class="contact">
          <svg viewBox="0 0 16 16"><circle cx="8" cy="8" r="6.5" fill="none" stroke="#1f3f78" stroke-width="1.6"/><path d="M1.5 8h13M8 1.5c-3 3-3 10 0 13M8 1.5c3 3 3 10 0 13" fill="none" stroke="#1f3f78" stroke-width="1.3"/></svg>
          www.trailhaus.ch
        </span>
      </div>
    </section>
  </main>
</body>
</html>
```